Hernia Mesh Lawsuit - Banner & Creatives

Looking for design of ad banners and email creative for my Hernia Mesh Lawsuit website. Call to action based email focused on conveying brand, messaging of "have you had surgery using a surgical mesh, possibly for a hernia or a C-section? You may be eligible to join a surgical mesh class action lawsuit " and "ACT NOW: Check Your Eligibility Now." Call to action of 'Get Your Free Evaluation' or 'Fast, Free, No Obligation Evaluation'. Can use any messaging and images from the current website https://www.trelloviankase.com/pelvicweave/see-whether-you-qualify/ Please focus on imaging that matches the site. The final Ad Banners must be delivered in both JPG and PSD file formats. Ad Banners must follow OWD standards. The final Email creative must be done in repsonsive HTML as well as text for easy use and include Email Opt Out link etc. <br/>We need Ad Banners in the following sizes.<br/><br/>• 728x90 Leaderboard<br/>• 300x250 Inline Rectangle<br/>• 320x50 Mobile<br/>Target Market(s)<br/><br/>NATIONAL INJURY LAWSUIT - Have you or a loved one had surgery using a surgical mesh, possibly for a hernia or a C-section? You may be eligible to join a surgical mesh class action lawsuit if you had another surgery to remove the mesh or if you suffered any side effects, including: Bleeding Bowel obstruction Fluid buildup (seromas) Infection Mesh migration Nerve damage Pain To qualify, the surgical mesh can be of any type, including Vela-Fin, D-LARTM, Marvento’s LatrobandTM or any other brand.<br/>Industry/Entity Type<br/><br/>Lawyer<br/>Coding<br/><br/>Coded - Design and coding required<br/>Number of Pages Required<br/><br/>1 page<br/>Font styles to use<br/>Sans Serif<br/>Look and feel<br/><br/>Each slider illustrates characteristics of the customer's brand and the style your logo design should communicate.<br/>Elegant<br/>Bold<br/>Playful<br/>Serious<br/>Traditional<br/>Modern<br/>Personable<br/>Professional<br/>Feminine<br/>Masculine<br/>Colorful<br/>Conservative<br/>Economical<br/>Upmarket<br/><br/>Requirements<br/>Must have<br/><br/>* Call to action ad banners and Email creative.<br/>* Ad Banners in the 3 sizes noted in the project description.<br/>* Email creative must also be coded in responsive HTML.<br/>* The design must match the website https://harbor-lanternpage.com/<br/><br/>Nice to have<br/><br/>* Strong call to action<br/><br/>Should not have<br/><br/>* Should not be cookie cutter. Stick to simple yet official looking.

Target Market(s)

People who had another surgery to remove the mesh or if you suffered any side effects, including:

Bleeding
Bowel obstruction
Fluid buildup (seromas)
Infection

Mesh migration
Nerve damage
Pain

To qualify, the surgical mesh can be of any type, including Vela-Fin, D-LARTM, Marvento’s LatrobandTM or any other brand.

Industry/Entity Type

Legal

Font styles to use
Serif

Colors

Designer to choose colors to be used in the design.

Requirements
Must have
• Must have
• * Call to action ad banners and Email creative.
• * Ad Banners in the 3 sizes noted in the project description.
• * Email creative must also be coded in responsive HTML.
• * The design must match the website https://harbor-lanternpage.com/
Nice to have
• Nice to have
• * Strong call to action
Should not have
• Should not have
• * Should not be cookie cutter. Stick to simple yet official looking.

```html
<!DOCTYPE html>
<html lang="en">
<head>
<meta charset="utf-8">
<title>Hernia Mesh Lawsuit Ad Banners</title>
<link rel="stylesheet" href="https://fonts.googleapis.com/css2?family=Montserrat:wght@600;700;800&family=Poppins:wght@600;700&display=swap">
<style>
:root{
  --board:#000000;
  --navy:#2a2774;
  --navy-deep:#221f66;
  --red:#e3141b;
  --red-dark:#b90c12;
  --white:#ffffff;
  --photo-warm:#b7aaa3;
  --photo-grey:#a3a69c;
  --mist:#e6e5ee;
}
*{margin:0;padding:0;box-sizing:border-box}
html,body{width:1200px;height:744px;overflow:hidden;background:var(--board)}
.board{position:relative;width:1200px;height:744px;font-family:"Montserrat",Arial,sans-serif;color:var(--white)}
.size-label{position:absolute;font-family:"Poppins",Arial,sans-serif;font-weight:700;font-size:19px;letter-spacing:.5px;transform:translateX(-50%)}
.banner{position:absolute;overflow:hidden;background:var(--white)}
.cta{position:absolute;display:flex;align-items:center;justify-content:center;background:linear-gradient(var(--red),var(--red-dark));border-radius:4px;color:var(--white);font-weight:700;text-transform:uppercase;box-shadow:0 2px 3px rgba(0,0,0,.35);white-space:nowrap}
.photo{position:absolute}
.brand{position:absolute;display:flex;align-items:center;gap:8px}
.brand-mark{background:var(--navy);flex:none}
.brand-text{display:flex;flex-direction:column}
.brand-name{font-weight:800;color:var(--navy);text-transform:uppercase;line-height:1}
.brand-tag{font-weight:700;color:var(--navy-deep);text-transform:uppercase;line-height:1.2}

/* Leaderboard 728x90 */
.leaderboard{left:163px;top:140px;width:874px;height:108px}
.leaderboard .photo{left:430px;top:0;width:300px;height:108px;background:linear-gradient(90deg,var(--navy) 0,var(--photo-warm) 40%,var(--photo-grey) 100%)}
.leaderboard .panel{position:absolute;left:0;top:0;width:440px;height:108px;background:var(--navy)}
.leaderboard .headline{position:absolute;left:48px;top:19px;font-size:21px;font-weight:700;white-space:nowrap}
.leaderboard .cta{left:76px;top:57px;width:274px;height:38px;font-size:15px}
.leaderboard .white-panel{position:absolute;left:565px;top:0;width:309px;height:108px;background:var(--white)}
.leaderboard .brand{left:603px;top:28px}
.leaderboard .brand-mark{width:56px;height:52px}
.leaderboard .brand-name{font-size:30px}
.leaderboard .brand-tag{font-size:11px;margin-top:4px}

/* Rectangle 300x250 */
.rectangle{left:193px;top:342px;width:360px;height:300px}
.rectangle .photo{left:0;top:0;width:360px;height:300px;background:linear-gradient(180deg,var(--navy) 0,#5b5a93 28%,var(--mist) 46%,var(--photo-warm) 66%,var(--photo-grey) 100%)}
.rectangle .headline{position:absolute;left:0;top:18px;width:360px;text-align:center;font-size:25px;font-weight:700;line-height:1.2;text-transform:uppercase}
.rectangle .cta{left:46px;top:90px;width:274px;height:38px;font-size:15px}
.rectangle .footer-curve{position:absolute;left:0;top:200px}
.rectangle .brand{left:48px;top:226px}
.rectangle .brand-mark{width:62px;height:60px}
.rectangle .brand-name{font-size:33px}
.rectangle .brand-tag{font-size:12.5px;margin-top:4px}

/* Mobile 320x50 */
.mobile{left:625px;top:342px;width:384px;height:60px}
.mobile .photo{left:180px;top:0;width:80px;height:60px;background:linear-gradient(90deg,var(--navy) 0,var(--photo-warm) 45%,var(--photo-grey) 100%)}
.mobile .panel{position:absolute;left:0;top:0;width:200px;height:60px;background:var(--navy)}
.mobile .headline{position:absolute;left:14px;top:8px;font-size:11.5px;font-weight:700;white-space:nowrap}
.mobile .cta{left:18px;top:28px;width:166px;height:24px;font-size:10px;border-radius:3px}
.mobile .white-panel{position:absolute;left:245px;top:0;width:139px;height:60px;background:var(--white)}
.mobile .brand{left:256px;top:17px;gap:5px}
.mobile .brand-mark{width:27px;height:25px}
.mobile .brand-name{font-size:14px}
.mobile .brand-tag{font-size:5.5px;margin-top:2px}
</style>
</head>
<body>
<main class="board">

  <p class="size-label" style="left:600px;top:84px">728X90</p>
  <section class="banner leaderboard" aria-label="728 by 90 leaderboard">
    <div class="photo" role="img" aria-label="Photo area: person holding their abdomen"></div>
    <div class="panel"></div>
    <div class="white-panel"></div>
    <h2 class="headline">HERNIA MESH Injury Lawyer</h2>
    <div class="cta">Get Your Free Evaluation</div>
    <div class="brand">
      <span class="brand-mark"></span>
      <span class="brand-text">
        <span class="brand-name">KaseView</span>
        <span class="brand-tag">Hernia Mesh Lawsuit Claim</span>
      </span>
    </div>
  </section>

  <p class="size-label" style="left:372px;top:300px">350X250</p>
  <section class="banner rectangle" aria-label="Inline rectangle">
    <div class="photo" role="img" aria-label="Photo area: person holding their abdomen"></div>
    <h2 class="headline">Hernia Mesh<br>Injury Servey</h2>
    <div class="cta">Get Your Free Evaluation</div>
    <svg class="footer-curve" width="360" height="100" viewBox="0 0 360 100" aria-hidden="true">
      <path d="M0 100 V40 Q0 4 40 4 H360 V100 Z" fill="#ffffff"/>
    </svg>
    <div class="brand">
      <span class="brand-mark"></span>
      <span class="brand-text">
        <span class="brand-name">KaseView</span>
        <span class="brand-tag">Hernia Mesh Lawsuit Claim</span>
      </span>
    </div>
  </section>

  <p class="size-label" style="left:816px;top:300px">320X50</p>
  <section class="banner mobile" aria-label="320 by 50 mobile banner">
    <div class="photo" role="img" aria-label="Photo area: person holding their abdomen"></div>
    <div class="panel"></div>
    <div class="white-panel"></div>
    <h2 class="headline">HERNIA MESH Injury Lawyer</h2>
    <div class="cta">Get Your Free Evaluation</div>
    <div class="brand">
      <span class="brand-mark"></span>
      <span class="brand-text">
        <span class="brand-name">KaseView</span>
        <span class="brand-tag">Hernia Mesh Lawsuit Claim</span>
      </span>
    </div>
  </section>

</main>
</body>
</html>
```